WordPress Website Design - Tolvey Auction

Need a WordPress design for an auction company wanting a responsive, simple and easy to use site.
Sites the client mentions liking - www.brindlegavel.example, http://www.quellor.example and http://www.pardwick.example/. The logo is attached. Site color can be changed to suit your design. Also consider the attached graphic for email lists.

Industry/Entity Type

It Company

Number of Pages Required

1 page

Font styles to use
Serif
Sans Serif

Requirements
Must have
• Will be graphic intensive with full width slideshow. tagline to be used – “Let Our Experience Work for You! The background of the site can be the background of the attached image. The feel of the site can be the attached email template.
• Navigation: 1)Home 2) Tolvey Services 3) Featured Projects 4) Results 5) Buying/Selling 6) About Tolvey 7) Contact us
• Colors will be those on current site and those in the email template.
• Calls to action on the homepage:1) Marketing Consultation, 2) Marketing Plan Implementation, 3) Coordination of Related Marketing Services, 4)Featured Projects, 5) Negotiated Sales
• widgets can include upcoming auctions, email signup, news & events
• Choice of the company logo to use- light or dark.
• Footer will have contact info, a testimonial widget,and associated logos (attached)
• contact info:
• Tolvey Companies, Inc
• P.O. Box 4382
• Rochester, MN 55961
• tolvey@tolveycompanies.example
• (507) 555-0187 • Fax (507) 555-0143
Nice to have
• Use of drop down menus - under "Results"
• 1) Auction Results
• 2) Sales results

```html
<!DOCTYPE html>
<html lang="en">
<head>
<meta charset="utf-8">
<title>Tolvey Companies</title>
<link rel="stylesheet" href="https://fonts.googleapis.com/css2?family=Open+Sans:wght@400;600;700;800&family=Playfair+Display:wght@400;700&display=swap">
<style>
:root{
  --bg:#2a1e16;
  --header:#241911;
  --panel:#1a130e;
  --panel-line:#3c2e22;
  --gold:#c9a24c;
  --tan:#b8914c;
  --red:#c3261c;
  --text:#e8e0d6;
  --muted:#b0a495;
  --white:#ffffff;
}
*{box-sizing:border-box;margin:0;padding:0}
html,body{width:829px;height:1200px;overflow:hidden}
body{background:var(--bg);font-family:"Open Sans",Arial,sans-serif;color:var(--text);position:relative}
.site-header{position:absolute;left:0;top:0;width:829px;height:88px;background:linear-gradient(#2e2016,var(--header))}
.brand{position:absolute;left:32px;top:16px;display:flex;align-items:center;gap:8px}
.brand-mark{width:14px;height:14px;background:var(--gold)}
.brand-name{font-family:"Playfair Display",Georgia,serif;font-weight:700;font-size:26px;color:var(--gold);line-height:1}
.social{position:absolute;left:604px;top:16px;display:flex;gap:10px}
.social span{width:26px;height:26px;border-radius:50%;background:#cfc8bf;display:block}
.contact-top{position:absolute;left:676px;top:14px;font-size:10px;color:var(--text);line-height:22px}
.contact-top div{display:flex;align-items:center;gap:6px}
.contact-top svg{width:14px;height:14px}
.hero{position:absolute;left:0;top:88px;width:829px;height:326px;background:radial-gradient(ellipse at 50% 30%,#7a5a3c 0%,#4a3424 45%,#1d140d 100%)}
.main-nav{position:absolute;left:0;top:0;width:829px;height:18px;background:rgba(20,14,9,.8);display:flex;justify-content:center;gap:34px;font-size:8.5px;font-weight:700;letter-spacing:.5px;line-height:18px;color:var(--white)}
.main-nav .has-drop{position:relative}
.drop{position:absolute;left:-4px;top:18px;width:92px;background:rgba(20,14,9,.9);font-weight:400;font-size:8px;letter-spacing:0}
.drop div{padding:0 6px;line-height:14px}
.drop div:first-child{background:var(--tan)}
.tagline{position:absolute;top:178px;width:100%;text-align:center;font-size:24px;font-weight:800;letter-spacing:1px;color:var(--white);text-shadow:0 2px 4px rgba(0,0,0,.6)}
.signup{position:absolute;left:0;top:414px;width:829px;height:68px;background:var(--tan);display:flex;align-items:center;padding-left:72px;gap:22px}
.signup h2{font-family:"Playfair Display",Georgia,serif;font-weight:400;font-size:34px;color:var(--white)}
.signup .field{width:168px;height:24px;background:var(--white);font-size:8px;color:#999;padding-left:6px;line-height:24px}
.signup .btn{background:var(--red);color:var(--white);font-size:12px;font-weight:600;padding:0 14px;line-height:26px}
.cta-list{position:absolute;left:72px;top:518px;width:222px;background:var(--panel);border:1px solid var(--panel-line);padding:8px 12px}
.cta-list li{list-style:none;font-size:9.5px;line-height:32px;border-bottom:1px solid var(--panel-line);color:var(--text)}
.cta-list li:last-child{border-bottom:0}
.cta-list li::before{content:"\203A";color:var(--gold);margin-right:6px}
.welcome{position:absolute;left:318px;top:514px;width:440px}
.welcome h1{font-family:"Playfair Display",Georgia,serif;font-size:27px;color:var(--gold);font-weight:700;margin-bottom:10px}
.welcome p{font-size:9px;line-height:14px;color:var(--muted);margin-bottom:10px}
.listing{position:absolute;left:72px;width:462px;height:192px;background:var(--panel);border:1px solid var(--panel-line)}
.listing h3{font-size:10px;font-weight:700;color:var(--white);background:#120d09;line-height:24px;padding-left:10px}
.listing .photo{position:absolute;left:10px;top:34px;width:130px;height:96px;background:linear-gradient(#9fb6c8 0%,#c9b48e 55%,#5d7a3a 100%)}
.listing .actions{position:absolute;left:10px;top:138px;display:flex;gap:6px}
.listing .actions span{font-size:9px;font-weight:700;color:var(--white);background:var(--red);padding:0 12px;line-height:20px;border-radius:2px}
.listing .actions span:first-child{background:#4c3b2c}
.listing .info{position:absolute;left:154px;top:32px;width:296px;font-size:8.5px;line-height:13px;color:var(--muted)}
.listing .info .kind{color:var(--red);font-weight:700;font-size:10px;margin-bottom:4px}
.listing .info p{margin-bottom:6px}
.listing .info b{color:var(--text)}
.widget{position:absolute;left:546px;width:212px;background:var(--panel);border:1px solid var(--panel-line);padding:10px}
.widget h4{font-size:15px;font-weight:800;color:var(--white);margin-bottom:4px}
.widget .sub{font-size:7.5px;color:var(--gold);margin-bottom:6px}
.widget .feat-photo{width:190px;height:72px;background:linear-gradient(#8aa0b4,#6b6a58 60%,#3e3a2c)}
.widget .date{font-size:8.5px;line-height:12px;color:var(--muted);margin-top:6px}
.news-item{display:flex;gap:8px;margin-top:8px}
.news-item .thumb{width:62px;height:44px;flex:none;background:linear-gradient(#8da6b8,#c2ad86 60%,#5e7638)}
.news-item .when{font-size:8px;font-weight:700;color:var(--red)}
.news-item p{font-size:8px;line-height:11px;color:var(--muted)}
.site-footer{position:absolute;left:0;top:1122px;width:829px;height:78px;background:#150f0b;border-top:1px solid var(--panel-line)}
.address{position:absolute;left:72px;top:8px;font-size:7.5px;line-height:10.5px;color:var(--muted)}
.badges{position:absolute;left:556px;top:18px;display:flex;gap:14px}
.badges span{width:38px;height:38px;background:#8d8278;display:block}
.badges span:nth-child(2){border-radius:50%}
</style>
</head>
<body>
<header class="site-header">
  <div class="brand"><span class="brand-mark"></span><span class="brand-name">Tolvey Companies</span></div>
  <div class="social"><span></span><span></span></div>
  <div class="contact-top">
    <div><svg viewBox="0 0 16 16"><path d="M4 1l3 3-2 2c1 2 3 4 5 5l2-2 3 3-2 2C7 14 2 9 2 3z" fill="#c9a24c"/></svg>(850) 555-0172</div>
    <div><svg viewBox="0 0 16 16"><rect x="1" y="3" width="14" height="10" fill="none" stroke="#c9a24c" stroke-width="1.5"/><path d="M1 3l7 6 7-6" fill="none" stroke="#c9a24c" stroke-width="1.5"/></svg>office@tolveymail.example</div>
  </div>
</header>

<section class="hero" role="img" aria-label="Crowded auction hall with bidders seated facing the auctioneer">
  <nav class="main-nav">
    <span>HOME</span>
    <span class="has-drop">TOLVEY SERVICES
      <div class="drop"><div>Auction Results</div><div>Sales Results</div></div>
    </span>
    <span>FEATURED PROJECTS</span>
    <span>RESULTS</span>
    <span>BUYING/SELLING</span>
    <span>ABOUT TOLVEY</span>
    <span>CONTACT US</span>
  </nav>
  <div class="tagline">LET OUR EXPERIENCE WORK FOR YOU!</div>
</section>

<section class="signup">
  <h2>Email</h2>
  <div class="field">Your Name</div>
  <div class="field">Email Address</div>
  <div class="btn">Subscribe Now</div>
</section>

<ul class="cta-list">
  <li>Marketing Consultation</li>
  <li>Marketing Plan Implementation</li>
  <li>Coordination of Related Marketing Services</li>
  <li>Featured Projects</li>
  <li>Negotiated Sales</li>
</ul>

<section class="welcome">
  <h1>Welcome to Tolvey Companies</h1>
  <p>Welcome to Tolvey Companies is simply dummy text of the printing and typesetting industry. Lorem Ipsum has been the industry's standard dummy text ever since the 1500s, when an unknown printer took a galley of type and scrambled it to make a type specimen book.</p>
  <p>It has survived not only five centuries, but also the leap into electronic typesetting, remaining essentially unchanged. It was popularised in the 1960s with the release of Letraset sheets containing Lorem Ipsum passages, and more recently with desktop publishing software. It was popularised in the 1960s with the release of Letraset sheets containing Lorem Ipsum passages, and more recently.</p>
</section>

<article class="listing" style="top:720px">
  <h3>2009 LARKSTONE TEXT OF THE PRINTING AND CRESTVIEW 34-FT. CAMPER</h3>
  <div class="photo" role="img" aria-label="Two-storey house with lawn and trees"></div>
  <div class="actions"><span>Details</span><span>Gallery</span></div>
  <div class="info">
    <div class="kind">LIVE ON-SITE AUCTION</div>
    <p><b>Begins:</b> Tuesday, April 23, 2013 at 10:00 AM CST</p>
    <p><b>Location:</b> Mountain Lake Area Entrance, 2560 N. Scenic Hwy 27. Text of the printing and typesetting industry. Lorem Ipsum has been the standard dummy text ever since the 1500s.</p>
    <p>Mountain Lake Hill Auction Property. Lake house has been the standard dummy text ever since 1500s.</p>
  </div>
</article>

<article class="listing" style="top:920px">
  <h3>2009 LARKSTONE TEXT OF THE PRINTING AND CRESTVIEW 34-FT. CAMPER</h3>
  <div class="photo" role="img" aria-label="Two-storey house with lawn and trees"></div>
  <div class="actions"><span>Details</span><span>Gallery</span></div>
  <div class="info">
    <div class="kind">LIVE ON-SITE AUCTION</div>
    <p><b>Begins:</b> Tuesday, April 23, 2013 at 10:00 AM CST</p>
    <p><b>Location:</b> Mountain Lake Area Entrance, 2560 N. Scenic Hwy 27. Text of the printing and typesetting industry. Lorem Ipsum has been the standard dummy text ever since the 1500s.</p>
    <p>Mountain Lake Hill Auction Property. Lake house has been the standard dummy text ever since 1500s.</p>
  </div>
</article>

<aside class="widget" style="top:720px;height:180px">
  <h4>FEATURED AUCTIONS</h4>
  <div class="sub">FACTORY 16 LOT | MACHINERY</div>
  <div class="feat-photo" role="img" aria-label="Industrial equipment lined up for auction"></div>
  <div class="date">Saturday, March 14, 2013 at 10:00 AM. Simply dummy text of the printing and typesetting industry.</div>
</aside>

<aside class="widget" style="top:910px;height:202px">
  <h4>NEWS &amp; EVENTS</h4>
  <div class="news-item">
    <div class="thumb" role="img" aria-label="House exterior"></div>
    <div><div class="when">OCTOBER 9, 2013</div><p>Lorem Ipsum is a dummy text it has a news or events.</p></div>
  </div>
  <div class="news-item">
    <div class="thumb" role="img" aria-label="House exterior"></div>
    <div><div class="when">OCTOBER 9, 2013</div><p>Lorem Ipsum is a dummy text it has a news or events.</p></div>
  </div>
</aside>

<footer class="site-footer">
  <div class="address">
    Tolvey Companies, Inc<br>
    P.O. Box 4382<br>
    Rochester, MN 55961<br>
    tolvey@tolveycompanies.example<br>
    (507) 555-0187 • Fax (507) 555-0143
  </div>
  <div class="badges"><span></span><span></span><span></span><span></span></div>
</footer>
</body>
</html>
```